we do all sorts of cleaning however bookings are limited!
why not chose the right cleaners for you!
pressure cleaning, window cleaning, office, end of lease clean, accommodation, industrial and commercial cleaning and house cleaning

Logo Text

Bright Nest Cleaning Service

```html
<!DOCTYPE html>
<html lang="en">
<head>
<meta charset="utf-8">
<title>Bright Nest Cleaning Service – Business Cards</title>
<link href="https://fonts.googleapis.com/css2?family=Open+Sans:wght@400;600;800&family=Great+Vibes&display=swap" rel="stylesheet">
<style>
  :root {
    --page: #2a2b2e;
    --card-black: #1b1b1c;
    --sky: #05b5f2;
    --sky-deep: #1a8cf5;
    --leaf: #8fd13b;
    --white: #ffffff;
  }
  * { margin: 0; padding: 0; box-sizing: border-box; }
  html, body {
    width: 1200px; height: 840px; overflow: hidden;
    background: var(--page);
    font-family: "Open Sans", Arial, sans-serif;
  }
  .stage {
    width: 1200px; height: 840px;
    display: flex; align-items: center; justify-content: center; gap: 40px;
  }
  .card {
    position: relative;
    width: 540px; height: 308px;
    border-radius: 22px;
    background: var(--card-black);
    overflow: hidden;
    color: var(--white);
    box-shadow: 0 18px 40px rgba(0,0,0,.45);
  }

  /* Brand name (stand-in for logo) */
  .brand {
    font-family: "Open Sans", Arial, sans-serif;
    font-weight: 800;
    color: var(--sky);
    text-align: center;
    line-height: 1.05;
    display: flex; align-items: center; justify-content: center; gap: 10px;
  }
  .brand-dot {
    width: 14px; height: 14px; border-radius: 50%;
    background: var(--leaf); flex: none;
  }

  /* Back card */
  .card-back .brand { padding-top: 34px; font-size: 30px; }
  .card-back .brand-sub { display: block; font-size: 13px; letter-spacing: 2px; }
  .intro {
    text-align: center; font-size: 14.5px; margin-top: 22px;
  }
  .band {
    margin-top: 10px;
    background: var(--sky);
    text-align: center;
    font-weight: 800; font-size: 17px;
    padding: 7px 0;
  }
  .services {
    list-style: none;
    display: flex; flex-wrap: wrap; justify-content: center;
    gap: 4px 14px;
    padding: 14px 36px 0;
    font-size: 14px;
  }
  .services li { display: flex; align-items: center; gap: 6px; }
  .services li::before {
    content: ""; width: 8px; height: 8px; border-radius: 50%;
    background: var(--leaf);
  }

  /* Front card */
  .card-front .wave { position: absolute; inset: 0; }
  .card-front .brand {
    position: absolute; top: 44px; left: 120px; width: 340px;
    flex-direction: column; gap: 2px; font-size: 34px;
  }
  .card-front .brand-row { display: flex; align-items: center; gap: 10px; }
  .card-front .brand-sub { font-size: 14px; letter-spacing: 2.5px; }
  .person {
    position: absolute; left: 120px; bottom: 46px; width: 200px;
    text-align: center;
  }
  .person-name {
    font-family: "Great Vibes", cursive;
    font-size: 42px; line-height: 1;
  }
  .person-role { font-size: 15px; margin-top: 4px; }
  .divider {
    position: absolute; left: 330px; bottom: 44px;
    width: 1px; height: 74px; background: rgba(255,255,255,.8);
  }
  .contact {
    position: absolute; left: 344px; bottom: 48px;
    list-style: none; font-size: 13.5px; line-height: 1.75;
  }
  .contact li { display: flex; align-items: center; gap: 7px; }
  .contact svg { width: 13px; height: 13px; flex: none; }
</style>
</head>
<body>
<main class="stage">

  <section class="card card-back">
    <div class="brand">
      <span class="brand-dot"></span>
      <span>Bright Nest<span class="brand-sub">CLEANING SERVICE</span></span>
    </div>
    <p class="intro">we do all sorts of cleaning however bookings are limited!</p>
    <p class="band">why not chose the right cleaners for you!</p>
    <ul class="services">
      <li>Pressure Cleaning</li>
      <li>Window Cleaning</li>
      <li>Office</li>
      <li>End Of Lease Clean</li>
      <li>Accommodation</li>
      <li>Industrial And Commercial Cleaning</li>
      <li>House Cleaning</li>
    </ul>
  </section>

  <section class="card card-front">
    <svg class="wave" viewBox="0 0 540 308" aria-hidden="true">
      <defs>
        <linearGradient id="blueFill" x1="0" y1="1" x2="1" y2="0">
          <stop offset="0" stop-color="#1a8cf5"/>
          <stop offset=".35" stop-color="#05b5f2"/>
          <stop offset="1" stop-color="#05b5f2"/>
        </linearGradient>
        <linearGradient id="swoosh" x1="0" y1="0" x2="1" y2="0">
          <stop offset="0" stop-color="#05b5f2"/>
          <stop offset=".5" stop-color="#05b5f2"/>
          <stop offset=".62" stop-color="#8fd13b"/>
          <stop offset="1" stop-color="#8fd13b"/>
        </linearGradient>
      </defs>
      <path d="M78 308 C 70 230, 130 205, 240 175 S 470 110, 540 70 L540 308 Z" fill="url(#blueFill)"/>
      <path d="M72 250 C 90 205, 150 190, 240 167 S 460 100, 528 40" fill="none" stroke="url(#swoosh)" stroke-width="6" stroke-linecap="round"/>
    </svg>

    <div class="brand">
      <span class="brand-row"><span class="brand-dot"></span>Bright Nest</span>
      <span class="brand-sub">CLEANING SERVICE</span>
    </div>

    <div class="person">
      <p class="person-name">Daniel Hartley</p>
      <p class="person-role">Managing Director</p>
    </div>
    <span class="divider"></span>
    <ul class="contact">
      <li>
        <svg viewBox="0 0 16 16" fill="#fff" aria-hidden="true"><path d="M3 1l3 3-1.5 2a9 9 0 0 0 5.5 5.5L12 10l3 3-2 2C6 15 1 10 1 3z"/></svg>
        044-987 650 312
      </li>
      <li>
        <svg viewBox="0 0 16 16" fill="none" stroke="#fff" stroke-width="1.6" aria-hidden="true"><rect x="1.5" y="3.5" width="13" height="9" rx="1"/><path d="M1.5 4l6.5 5 6.5-5"/></svg>
        hello@brightnestclean.com
      </li>
      <li>
        <svg viewBox="0 0 16 16" fill="none" stroke="#fff" stroke-width="1.4" aria-hidden="true"><circle cx="8" cy="8" r="6.5"/><path d="M1.5 8h13M8 1.5c-3 3.5-3 9.5 0 13M8 1.5c3 3.5 3 9.5 0 13"/></svg>
        www.brightnestclean.com
      </li>
    </ul>
  </section>

</main>
</body>
</html>
```